stars + comments Reviews website design (similar to grubly concept)

Please refer to attached logo and wire frames
----------------------------------------------------------------------------------------------------
we are a company based in egypt, seeking a design for a website that allows user to find doctors using search and filters.
also it allows user to review this doctor through providing comment and 1 to 5 stars
i need 4 main pages designs:
1- Doctors list/favorites list
2- Doctor view
3- Add doctor (3 steps)
4- Sign-in/sign up
5- Menu design
am into the colors teal/turquoise (though am open for different opinion)
i don't want the design theme to be doctors specific
am into the school of very clean, very neat, very simple
(chirpnet, pagecircle, snapmosaic designs are appealing to me)
Updates

Number of Pages Required

4 page

Font styles to use
Sans Serif

Colors
00a990
33b8a4

Requirements
Must have
• website will be bilingual/ bi-directional (English and Arabic)
• designer needs to provide another copy of the design with "right to left" orientation
• interactive button animation

```html
<!DOCTYPE html>
<html lang="en">
<head>
<meta charset="utf-8">
<title>Ratewell – Doctors</title>
<link href="https://fonts.googleapis.com/css2?family=Arimo:wght@400;700&display=swap" rel="stylesheet">
<style>
:root{
  --header:#045e5c;
  --filterbar:#191919;
  --filter-field:#a5a5a5;
  --page:#9d9c97;
  --card:#a9a8a3;
  --divider:#8f8e8a;
  --ink:#2b2b2b;
  --logo:#a9aaa9;
  --icon-dark:#1d1d1d;
  --icon-fav:#b22a35;
  --star-muted:#a88a10;
  --heart:#a3222e;
  --modal:#e92a40;
  --modal-frame:#6c6c6c;
  --star:#f7c10c;
  --white:#ffffff;
}
*{box-sizing:border-box;margin:0;padding:0}
html,body{width:1200px;height:929px;overflow:hidden}
body{position:relative;background:var(--page);font-family:"Arimo",Arial,sans-serif;color:var(--ink)}
.site-header{position:absolute;left:0;top:0;width:1200px;height:103px;background:var(--header)}
.brand{position:absolute;left:105px;top:20px;display:flex;align-items:center;gap:10px}
.brand-dot{width:40px;height:40px;border-radius:50%;background:var(--logo)}
.brand-name{font-size:50px;font-weight:700;color:var(--logo);letter-spacing:-1px;line-height:1}
.nav-icon{position:absolute;top:31px;width:50px;height:50px;border-radius:50%;background:var(--icon-dark);display:flex;align-items:center;justify-content:center}
.nav-icon.home{left:522px}
.nav-icon.favorites{left:646px;background:var(--icon-fav)}
.nav-icon.add-doctor{left:772px}
.account-menu{position:absolute;left:949px;top:37px;width:121px;height:35px;border:1px solid #8cb3b1;color:#b8cfce;font-size:15px;display:flex;align-items:center;justify-content:center;gap:8px}
.caret{width:0;height:0;border-left:5px solid transparent;border-right:5px solid transparent;border-top:5px solid currentColor}
.filter-bar{position:absolute;left:0;top:103px;width:1200px;height:76px;background:var(--filterbar);border-bottom:5px solid #b0afab;height:81px}
.field{position:absolute;top:22px;height:30px;background:var(--filter-field);font-size:15px;color:var(--ink);padding:0 8px;display:flex;align-items:center;justify-content:space-between}
.field .caret{color:#2b2b2b}
.result-count{position:absolute;left:138px;top:221px;font-size:14px;font-weight:700;color:#1e1e1e}
.doctor-list{position:absolute;left:138px;top:251px;width:915px;height:606px;background:var(--card);box-shadow:0 1px 3px rgba(0,0,0,.2)}
.doctor{position:absolute;left:0;width:915px;height:143px;border-bottom:1px solid var(--divider)}
.doctor:last-child{border-bottom:none}
.doctor-photo{position:absolute;left:26px;top:30px;width:99px;height:97px;background:linear-gradient(160deg,#8a8578,#5d5a52)}
.doctor-photo.warm{background:linear-gradient(160deg,#b39a45,#7a5e2c)}
.doctor-info{position:absolute;left:140px;top:40px;font-size:15px;line-height:28px;color:#2e2e2e}
.doctor-rating{position:absolute;left:696px;top:42px;display:flex;align-items:center;gap:12px;font-size:15px;color:#2e2e2e}
.fav{position:absolute;left:822px;top:84px}
.footer{position:absolute;left:0;top:881px;width:1200px;text-align:center;font-size:13px;color:#222}
.review-modal{position:absolute;left:355px;top:351px;width:549px;height:270px;border:4px solid var(--modal-frame);border-radius:6px;background:var(--modal);color:var(--white)}
.close{position:absolute;left:511px;top:13px;width:19px;height:19px;border-radius:50%;background:#000;display:flex;align-items:center;justify-content:center}
.review-total{position:absolute;left:73px;top:36px;font-size:15px}
.criteria{position:absolute;left:30px;top:74px;list-style:none}
.criteria li{display:flex;align-items:center;height:44px;font-size:15px}
.criteria svg{margin-right:16px}
.modal-divider{position:absolute;left:263px;top:41px;width:1px;height:170px;background:rgba(255,255,255,.45)}
.comments{position:absolute;left:286px;top:56px;width:230px}
.comment{margin-bottom:19px}
.comment h3{font-size:15px;font-weight:700;margin-bottom:4px}
.comment p{font-size:13px;line-height:20px}
</style>
</head>
<body>
<svg width="0" height="0" style="position:absolute">
  <defs>
    <symbol id="star" viewBox="0 0 20 20"><polygon points="10,1 12.6,7 19,7.6 14.2,12 15.6,18.5 10,15.2 4.4,18.5 5.8,12 1,7.6 7.4,7" fill="currentColor"/></symbol>
    <clipPath id="half"><rect x="0" y="0" width="10" height="20"/></clipPath>
    <symbol id="star-half" viewBox="0 0 20 20"><polygon points="10,1 12.6,7 19,7.6 14.2,12 15.6,18.5 10,15.2 4.4,18.5 5.8,12 1,7.6 7.4,7" fill="none" stroke="currentColor" stroke-width="1.3"/><polygon clip-path="url(#half)" points="10,1 12.6,7 19,7.6 14.2,12 15.6,18.5 10,15.2 4.4,18.5 5.8,12 1,7.6 7.4,7" fill="currentColor"/></symbol>
    <symbol id="rating" viewBox="0 0 110 20"><use href="#star" x="0" width="20" height="20"/><use href="#star" x="22" width="20" height="20"/><use href="#star" x="44" width="20" height="20"/><use href="#star" x="66" width="20" height="20"/><use href="#star-half" x="88" width="20" height="20"/></symbol>
    <symbol id="heart" viewBox="0 0 30 28"><path d="M15 26C6 19 2 14.5 2 9.2 2 5.2 5 2.2 8.7 2.2c2.7 0 4.7 1.5 6.3 3.7 1.6-2.2 3.6-3.7 6.3-3.7C25 2.2 28 5.2 28 9.2 28 14.5 24 19 15 26z"/></symbol>
  </defs>
</svg>

<header class="site-header">
  <div class="brand"><span class="brand-dot"></span><span class="brand-name">Ratewell</span></div>
  <a class="nav-icon home" aria-label="Home"><svg width="30" height="28" viewBox="0 0 30 28"><path d="M15 3 2 14h4v11h7v-7h4v7h7V14h4z" fill="#c9c9c9"/></svg></a>
  <a class="nav-icon favorites" aria-label="Favorites"><svg width="28" height="26" viewBox="0 0 30 28"><use href="#heart" fill="#d9d9d9"/></svg></a>
  <a class="nav-icon add-doctor" aria-label="Add doctor"><svg width="28" height="28" viewBox="0 0 28 28"><circle cx="11" cy="8" r="5" fill="#c9c9c9"/><path d="M2 24c0-6 4-9 9-9s7 2 8 4v5z" fill="#c9c9c9"/><circle cx="20" cy="20" r="6" fill="#c9c9c9"/><path d="M20 16.5v7M16.5 20h7" stroke="#1d1d1d" stroke-width="2"/></svg></a>
  <div class="account-menu">Admin Sam <span class="caret"></span></div>
</header>

<nav class="filter-bar">
  <div class="field" style="left:111px;width:171px">Search <svg width="20" height="20" viewBox="0 0 20 20"><circle cx="8" cy="8" r="6" fill="none" stroke="#111" stroke-width="2.4"/><path d="M12.5 12.5 18 18" stroke="#111" stroke-width="2.6"/></svg></div>
  <div class="field" style="left:312px;width:150px">Specialization <span class="caret"></span></div>
  <div class="field" style="left:490px;width:153px">Sub-specialization <span class="caret"></span></div>
  <div class="field" style="left:673px;width:125px">Gender <span class="caret"></span></div>
  <div class="field" style="left:829px;width:125px">Gender <span class="caret"></span></div>
  <div class="field" style="left:987px;width:101px">Rating <span class="caret"></span></div>
</nav>

<p class="result-count">15,123 Doctors</p>

<section class="doctor-list">
  <article class="doctor" style="top:0;height:148px">
    <div class="doctor-photo" role="img" aria-label="Portrait of the doctor"></div>
    <div class="doctor-info">Karim Adel (1 Km away)<br>Anesthesiogist<br>41 Cedar Lane, Westbrook</div>
    <div class="doctor-rating"><svg width="110" height="20" style="color:var(--star-muted)"><use href="#rating"/></svg>(123)</div>
    <svg class="fav" width="30" height="28" viewBox="0 0 30 28"><use href="#heart" fill="none" stroke="#222" stroke-width="1.4"/></svg>
  </article>
  <article class="doctor" style="top:148px;height:142px">
    <div class="doctor-photo warm" style="top:24px" role="img" aria-label="Portrait of the doctor"></div>
    <div class="doctor-info" style="top:30px">Karim Adel (1 Km away)<br>Anesthesiogist<br>41 Cedar Lane, Westbrook</div>
    <div class="doctor-rating" style="top:37px"><svg width="110" height="20" style="color:var(--star-muted)"><use href="#rating"/></svg>(123)</div>
    <svg class="fav" style="top:78px" width="30" height="28" viewBox="0 0 30 28"><use href="#heart" fill="var(--heart)"/></svg>
  </article>
  <article class="doctor" style="top:290px;height:145px">
    <div class="doctor-photo" style="top:27px" role="img" aria-label="Portrait of the doctor"></div>
    <div class="doctor-info" style="top:33px">Karim Adel (1 Km away)<br>Anesthesiogist<br>41 Cedar Lane, Westbrook</div>
    <div class="doctor-rating" style="top:40px"><svg width="110" height="20" style="color:var(--star-muted)"><use href="#rating"/></svg>(123)</div>
    <svg class="fav" style="top:81px" width="30" height="28" viewBox="0 0 30 28"><use href="#heart" fill="var(--heart)"/></svg>
  </article>
  <article class="doctor" style="top:435px;height:171px">
    <div class="doctor-photo" style="top:26px" role="img" aria-label="Portrait of the doctor"></div>
    <div class="doctor-info" style="top:33px">Karim Adel (1 Km away)<br>Anesthesiogist<br>41 Cedar Lane, Westbrook</div>
    <div class="doctor-rating" style="top:40px"><svg width="110" height="20" style="color:var(--star-muted)"><use href="#rating"/></svg>(123)</div>
    <svg class="fav" style="top:80px" width="30" height="28" viewBox="0 0 30 28"><use href="#heart" fill="var(--heart)"/></svg>
  </article>
</section>

<footer class="footer">Copyright © 2015 The Ratewell. Powered by PressKit and Makeworks</footer>

<div class="review-modal" role="dialog" aria-label="Doctor reviews">
  <span class="close"><svg width="9" height="9" viewBox="0 0 9 9"><path d="M1 1l7 7M8 1 1 8" stroke="#fff" stroke-width="2"/></svg></span>
  <p class="review-total">(211)</p>
  <ul class="criteria">
    <li><svg width="110" height="20" style="color:var(--star)"><use href="#rating"/></svg>Attitude</li>
    <li><svg width="110" height="20" style="color:var(--star)"><use href="#rating"/></svg>Waiting time</li>
    <li><svg width="110" height="20" style="color:var(--star)"><use href="#rating"/></svg>Facility</li>
  </ul>
  <div class="modal-divider"></div>
  <div class="comments">
    <div class="comment"><h3>Karim Adel</h3><p>text of the printing and typesetting industry. Lorem Ipsum</p></div>
    <div class="comment"><h3>Salma Fathy</h3><p>text of the printing and typesetting industry. Lorem Ipsum</p></div>
  </div>
</div>
</body>
</html>
```